Cards and what not
Project: Stationary
Stationary - Consulting
Stationary
Simple
Tomaso Reyk Halden
CEO
Do not want to use an address please.
833-LUMACORP (833-586-2267)
th@lumacorp.com
www.lumacorp.com
Please make the font large enough to more easily read. Some cards...the font is too small. Please use our logo as well. I prefer a vertical design but open to horizontal too. Many thanks :)
lumacorp lumacorp
I am looking for a vertical design while open to checking out horizontal designs (for the business card). Thanks guys (and ladies)

```html
<!DOCTYPE html>
<html lang="en">
<head>
<meta charset="utf-8">
<title>Lumacorp business cards</title>
<link rel="stylesheet" href="https://fonts.googleapis.com/css2?family=Raleway:wght@400;600&display=swap">
<style>
  :root {
    --stage: #ecebe8;
    --card: #ffffff;
    --cyan: #35b9e2;
    --band-grey: #b8babd;
    --ink: #5b5e62;
    --light: #ffffff;
  }
  * { margin: 0; padding: 0; box-sizing: border-box; }
  html, body { width: 1200px; height: 982px; overflow: hidden; }
  body {
    background: var(--stage);
    font-family: "Raleway", sans-serif;
    position: relative;
  }
  .card {
    position: absolute;
    width: 540px;
    height: 310px;
    background: var(--card);
    box-shadow: 0 6px 18px rgba(0,0,0,0.18);
    overflow: hidden;
  }
  .card--front { left: 50px; top: 200px; }
  .card--back { left: 610px; top: 470px; }
  .card__bands { position: absolute; inset: 0; }
  .brand {
    position: absolute;
    display: flex;
    flex-direction: column;
    align-items: center;
  }
  .card--front .brand { left: 60px; top: 48px; }
  .card--back .brand { left: 0; right: 0; top: 118px; }
  .brand__row { display: flex; align-items: center; gap: 10px; }
  .brand__dot {
    width: 16px; height: 16px;
    border-radius: 50%;
    background: var(--band-grey);
  }
  .brand__name {
    font-size: 34px;
    font-weight: 400;
    letter-spacing: 3px;
    color: var(--cyan);
    text-transform: uppercase;
  }
  .brand__tagline {
    margin-top: 4px;
    font-size: 8px;
    letter-spacing: 3px;
    color: var(--ink);
    text-transform: uppercase;
  }
  .person {
    position: absolute;
    left: 36px;
    bottom: 28px;
    color: var(--light);
  }
  .person__name { font-size: 16px; font-weight: 600; letter-spacing: 1px; text-transform: uppercase; }
  .person__title { font-size: 11px; letter-spacing: 2px; text-transform: uppercase; margin-top: 3px; }
  .contact {
    position: absolute;
    right: 28px;
    top: 150px;
    list-style: none;
    text-align: right;
    color: var(--light);
    font-size: 12px;
    line-height: 1.9;
  }
</style>
</head>
<body>
  <section class="card card--front">
    <svg class="card__bands" width="540" height="310" viewBox="0 0 540 310">
      <path d="M0,214 C200,186 400,104 540,22 L540,310 L0,310 Z" fill="var(--band-grey)"/>
      <path d="M0,230 C200,202 400,122 540,42 L540,310 L0,310 Z" fill="var(--cyan)"/>
    </svg>
    <div class="brand">
      <div class="brand__row"><span class="brand__dot"></span><span class="brand__name">Lumacorp</span></div>
      <div class="brand__tagline">Consulting Services Group</div>
    </div>
    <ul class="contact">
      <li>833-LUMACORP (833-586-2267)</li>
      <li>th@lumacorp.com</li>
      <li>www.lumacorp.com</li>
    </ul>
    <div class="person">
      <div class="person__name">Tomaso Reyk Halden</div>
      <div class="person__title">CEO</div>
    </div>
  </section>

  <section class="card card--back">
    <div class="brand">
      <div class="brand__row"><span class="brand__dot"></span><span class="brand__name">Lumacorp</span></div>
      <div class="brand__tagline">Consulting Services Group</div>
    </div>
  </section>
</body>
</html>
```